Gearloft forum banner

Need a banner ad for a forum relating to the motor car industry.
I have attached a sample banner , we need ours to be edited to suit our web site - gearloft-example.com.au
Image needs to be roughly 400px by 100px.
We would like to display information like the pic below named kelbanner but with a better design / colour / image combination.

```html
<!DOCTYPE html>
<html lang="en">
<head>
<meta charset="utf-8">
<title>Gearloft forum banner</title>
<link rel="stylesheet" href="https://fonts.googleapis.com/css2?family=Arimo:wght@400;700&family=Tinos:wght@700&display=swap">
<style>
  :root {
    --band-dark: #2a2a2c;
    --band-mid: #4a4a4e;
    --grey-light: #d9d9db;
    --grey-mid: #a9a9ad;
    --panel-white: #f4f4f4;
    --brand-red: #c8161d;
    --deep-red: #8e0c10;
    --text-dark: #1e1e1e;
    --text-white: #ffffff;
  }
  * { margin: 0; padding: 0; box-sizing: border-box; }
  html, body { width: 1200px; height: 300px; overflow: hidden; background: #fff; }
  .banner {
    position: relative;
    width: 1200px;
    height: 300px;
    overflow: hidden;
    font-family: "Arimo", Arial, sans-serif;
    background: linear-gradient(180deg, var(--grey-mid) 0%, var(--grey-light) 60%, #c4c4c6 100%);
    border: 2px solid #888;
  }
  .car-photo {
    position: absolute;
    left: 520px; top: 60px;
    width: 680px; height: 240px;
    background:
      radial-gradient(ellipse 300px 110px at 62% 78%, rgba(190,20,25,0.85), rgba(190,20,25,0) 70%),
      linear-gradient(180deg, #bdbdc0 0%, #9c9ca0 55%, #7d7d82 100%);
  }
  .top-band {
    position: absolute;
    left: 0; top: 0;
    width: 1200px; height: 90px;
    background: linear-gradient(180deg, var(--band-dark) 0%, var(--band-mid) 100%);
  }
  .brand {
    position: absolute;
    left: 18px; top: 8px;
    display: flex; align-items: center; gap: 12px;
  }
  .brand-mark {
    width: 22px; height: 22px;
    background: var(--brand-red);
  }
  .brand-name {
    font-weight: 700;
    font-size: 50px;
    letter-spacing: 2px;
    color: var(--text-white);
    text-transform: uppercase;
  }
  .brand-tagline {
    position: absolute;
    left: 20px; top: 66px;
    font-size: 15px;
    color: #cfcfcf;
    letter-spacing: 1px;
    text-transform: uppercase;
  }
  .services-panel {
    position: absolute;
    left: 0; top: 90px;
    width: 560px; height: 210px;
    background: linear-gradient(90deg, var(--panel-white) 0%, rgba(244,244,244,0.9) 60%, rgba(244,244,244,0) 100%);
  }
  .services {
    position: absolute;
    left: 22px; top: 124px;
    list-style: none;
  }
  .services li {
    display: flex; align-items: center;
    font-size: 27px;
    line-height: 40px;
    color: var(--text-dark);
  }
  .services li::before {
    content: "";
    width: 12px; height: 12px;
    background: var(--brand-red);
    margin-right: 14px;
  }
  .call {
    position: absolute;
    right: 30px; top: 12px;
    font-size: 30px;
    color: var(--text-white);
  }
  .headline {
    position: absolute;
    right: 30px; top: 62px;
    font-size: 54px;
    font-weight: 700;
    color: var(--text-white);
    text-shadow: 0 2px 4px rgba(0,0,0,0.5);
  }
  .subline {
    position: absolute;
    right: 30px; top: 128px;
    font-size: 24px;
    color: var(--text-white);
    text-shadow: 0 1px 3px rgba(0,0,0,0.6);
  }
  .price-box {
    position: absolute;
    right: 6px; bottom: 6px;
    width: 222px; height: 106px;
    background: linear-gradient(180deg, var(--brand-red) 0%, var(--deep-red) 100%);
    border: 2px solid rgba(255,255,255,0.7);
    text-align: right;
    padding: 6px 14px 0 0;
    color: var(--text-white);
  }
  .price-label { font-size: 28px; line-height: 30px; }
  .price-amount {
    font-family: "Tinos", "Times New Roman", serif;
    font-weight: 700;
    font-size: 66px;
    line-height: 66px;
  }
</style>
</head>
<body>
  <div class="banner">
    <div class="car-photo" role="img" aria-label="Red imported sports car photographed in a showroom"></div>
    <div class="top-band"></div>
    <div class="brand">
      <span class="brand-mark"></span>
      <span class="brand-name">Gearloft</span>
    </div>
    <div class="brand-tagline">quality vehicle import specialists</div>

    <div class="services-panel"></div>
    <ul class="services">
      <li>vehicle purchase</li>
      <li>shipping, customs</li>
      <li>compliance</li>
      <li>registration (if in VIC)</li>
    </ul>

    <div class="call">Call us - 0400 123 456</div>
    <div class="headline">Japan car import service</div>
    <div class="subline">visit us anytime at our showroom to learn more !</div>

    <div class="price-box">
      <div class="price-label">Special price</div>
      <div class="price-amount">$550</div>
    </div>
  </div>
</body>
</html>
```